Young Makers Competition Event For Teenagers Needs Promo Graphics

I am in need of graphics for 2019 Northmere Young Makers Festival. It is a Young Makers competition event for teenagers. I need graphics to make an 11x17 poster and a main title graphic that I can use for digital (social, 16x9 for screens, etc). Graphic should include the following 2 logos: the QW Brightpath logo (this is who we are) and the "circles" logo is the logo of Young Makers Festival so that can be incorporated but is not mandatory and does not need to be in color. Tag line for Young Makers is "Discover. Develop. Deploy." Again, this is optional. Looking for an artistic design - geometric shapes, bright colors, or something along those lines. Something that speaks to teenagers and especially creatives/Young Makers types. Additionally, Post should include:
Maple Ridge Chapel
March 29-30
(registration & cost info may be added to the poster before design is finalized; still working on those details)

```html
<!DOCTYPE html>
<html lang="en">
<head>
<meta charset="utf-8">
<title>Northmere Young Makers Festival</title>
<link rel="stylesheet" href="https://fonts.googleapis.com/css2?family=Poppins:wght@300;600;700&family=Oswald:wght@500&display=swap">
<style>
  :root {
    --navy: #1c1549;
    --deep-blue: #13356c;
    --orange: #f7941f;
    --yellow: #f0d11a;
    --sky: #a5c4cf;
    --hatch: #4a4478;
    --white: #ffffff;
  }
  * { margin: 0; padding: 0; box-sizing: border-box; }
  html, body { width: 776px; height: 1200px; overflow: hidden; background: var(--navy); }
  .poster {
    position: relative;
    width: 776px;
    height: 1200px;
    overflow: hidden;
    background: var(--navy);
    font-family: "Poppins", sans-serif;
  }
  .shapes { position: absolute; inset: 0; width: 776px; height: 1200px; display: block; }
  .brand {
    position: absolute;
    top: 62px;
    right: 86px;
    display: flex;
    align-items: center;
    gap: 12px;
    color: var(--white);
    font-family: "Poppins", sans-serif;
    font-weight: 600;
    font-size: 22px;
    letter-spacing: 0.2px;
  }
  .brand-dot {
    width: 40px; height: 40px;
    border-radius: 50%;
    border: 4px solid var(--white);
  }
  .title {
    position: absolute;
    right: 75px;
    top: 150px;
    text-align: right;
    color: var(--white);
  }
  .title-region {
    font-weight: 300;
    font-size: 46px;
    letter-spacing: 1px;
    line-height: 1;
    margin-bottom: 8px;
  }
  .title-main {
    font-weight: 700;
    font-size: 88px;
    line-height: 0.95;
    letter-spacing: 0.5px;
  }
  .tagline {
    position: absolute;
    left: 318px;
    top: 758px;
    list-style: none;
    color: var(--white);
    font-family: "Oswald", sans-serif;
    font-weight: 500;
    font-size: 58px;
    line-height: 80px;
    letter-spacing: 0.5px;
  }
  .tagline li { display: flex; align-items: center; gap: 28px; }
  .tagline li::before {
    content: "";
    width: 22px; height: 22px;
    border-radius: 50%;
    background: var(--white);
  }
  .event-info {
    position: absolute;
    right: 50px;
    top: 1080px;
    text-align: right;
    color: var(--navy);
    font-family: "Oswald", sans-serif;
    font-weight: 500;
    font-size: 36px;
    line-height: 42px;
  }
</style>
</head>
<body>
<main class="poster">
  <svg class="shapes" viewBox="0 0 500 773" preserveAspectRatio="none" aria-hidden="true">
    <!-- top-right corner triangle -->
    <polygon points="278,0 500,0 500,230" fill="var(--orange)"/>
    <!-- left arc block -->
    <path d="M0,0 H128 Q178,120 175,270 V440 H0 Z" fill="var(--orange)"/>
    <circle cx="-45" cy="222" r="110" fill="var(--deep-blue)"/>
    <polygon points="175,270 175,440 0,440" fill="var(--yellow)"/>
    <!-- middle-left band -->
    <polygon points="0,440 175,440 0,610" fill="var(--navy)"/>
    <polygon points="175,440 175,773 0,610" fill="var(--yellow)"/>
    <polygon points="0,610 175,773 0,773" fill="var(--orange)"/>
    <!-- lower-right panel -->
    <rect x="175" y="440" width="325" height="333" fill="var(--orange)"/>
    <rect x="175" y="675" width="325" height="98" fill="var(--sky)"/>
    <!-- right half-circle stack -->
    <path d="M500,325 A115,115 0 0 0 385,440 H500 Z" fill="var(--orange)"/>
    <path d="M500,395 A45,45 0 0 0 455,440 H500 Z" fill="var(--navy)"/>
    <path d="M385,440 A115,115 0 0 0 500,555 V440 Z" fill="var(--deep-blue)"/>
    <path d="M455,440 A45,45 0 0 0 500,485 V440 Z" fill="var(--yellow)"/>
  </svg>
  <svg class="shapes" viewBox="0 0 500 773" preserveAspectRatio="none" role="img" aria-label="Diagonal line texture in a triangle">
    <polygon points="175,268 385,440 175,440" fill="var(--hatch)"/>
  </svg>

  <div class="brand">
    <span>QW Brightpath</span>
    <span class="brand-dot"></span>
  </div>

  <h1 class="title">
    <span class="title-region" style="display:block">NORTHMERE</span>
    <span class="title-main" style="display:block">YOUNG<br>MAKERS<br>FESTIVAL</span>
  </h1>

  <ul class="tagline">
    <li>DISCOVER</li>
    <li>DEVELOP</li>
    <li>DEPLOY</li>
  </ul>

  <p class="event-info">MAPLE RIDGE CHAPEL<br>MARCH 29 - 30</p>
</main>
</body>
</html>
```